Culture consulting company business card - first step

I created a new venture called The Summit Ledger. It's focused on improving the organizational culture of companies and I have a logo, tag line and other basic info but I need an overall design theme I'll carry through to letterhead, marketing literature, direct mail post cards, whitepapers, video intros and my web site. The business card design is a trial to develop the theme and more projects will hopefully follow for the winner! This business will grow fast and I need a great design theme to leverage.

Target Market(s)

Target Market is both for profit and non profit businesses. Special emphasis on consulting companies, foundations and venture capital firms

Industry/Entity Type

Marketing

Requirements
Must have
• The Summit Ledger Logo
Name (Dan Prewitt)
Phone (555-417-6290)
E-mail (Dan@The-Summit-Ledger.example)
Web Site (www.The-Summit-Ledger.example)
Tag line in some way: "Culture Change with Clarity and Speed"
- Clarity and Speed should be in red with speed potentially in italics. The other words in black.

Front and back of card design - front has info above
Back should have The Summit Ledger logo and a list of areas we focus on with the red check mark image next to each. The areas are: Performance Improvement, Organizational Excellence, Strategic Alignment, Team Effectiveness, Onboarding, Leadership Development & Coaching

Overall key colors are in the logo (red & black)

NEED DESIGN FORMAT in a PHOTOSHOP / PSD FILE. Photoshop template from printer is attached. Needs to follow the diminsions / guidelines.
Nice to have
• Potentially "road" picture if it fits with a great theme
Should not have
• Needs to be veryprofessional looking but it's fine to come across as very innovative, interesting or unique. Need clear design / fonts and color theme I can carry through to other print and web formats.

```html
<!DOCTYPE html>
<html lang="en">
<head>
<meta charset="utf-8">
<title>The Summit Ledger – Business Card</title>
<link href="https://fonts.googleapis.com/css2?family=Questrial&display=swap" rel="stylesheet">
<style>
  :root{
    --brand-red:#d0132e;
    --deep-red:#8e0a18;
    --ink:#111111;
    --paper:#f1f0ef;
    --road-light:#e6e4e2;
    --road-mid:#b9b6b3;
    --road-dark:#7d7a77;
    --stage:#dcdcdc;
    --label:#444444;
  }
  html,body{margin:0;padding:0;}
  body{
    width:1200px;height:765px;overflow:hidden;position:relative;
    background:var(--stage);
    font-family:"Questrial",sans-serif;
  }
  .card{
    position:absolute;top:302px;width:575px;height:344px;
    border-radius:30px;overflow:hidden;
    box-shadow:0 6px 14px rgba(0,0,0,.25);
  }
  .card--front{left:17px;}
  .card--back{left:608px;}
  .side-label{
    position:absolute;top:686px;font-family:"Questrial",sans-serif;
    font-size:14px;letter-spacing:3px;color:var(--label);
  }
  .side-label--front{left:66px;}
  .side-label--back{left:659px;}

  /* Front */
  .road-photo{position:absolute;inset:0;}
  .road-photo--front{
    background:linear-gradient(180deg,var(--paper) 0%,var(--road-light) 25%,var(--road-mid) 60%,var(--road-light) 100%);
  }
  .tagline{
    position:absolute;left:30px;top:30px;margin:0;
    font-size:20px;font-weight:400;color:var(--ink);letter-spacing:.3px;
  }
  .tagline em{color:var(--brand-red);}
  .brand-name{
    position:absolute;left:28px;top:218px;width:190px;margin:0;
    font-size:24px;line-height:1.15;color:var(--brand-red);text-align:center;
  }
  .contact-panel{position:absolute;left:212px;top:140px;width:340px;height:185px;}
  .contact-panel svg{position:absolute;inset:0;}
  .holder-name{
    position:absolute;left:62px;top:27px;margin:0;font-size:24px;line-height:30px;color:var(--ink);
  }
  .contact-list{
    position:absolute;left:56px;top:84px;margin:0;padding:0;list-style:none;color:#fff;
  }
  .contact-list li{display:flex;align-items:center;gap:6px;height:22px;font-size:14px;white-space:nowrap;}
  .contact-list li.phone{font-size:20px;height:26px;}
  .contact-icon{width:14px;height:14px;background:var(--brand-red);border-radius:2px;flex:none;}

  /* Back */
  .road-photo--back{
    background:linear-gradient(180deg,var(--road-light) 0%,var(--road-mid) 45%,var(--road-dark) 100%);
  }
  .back-band{position:absolute;inset:0;}
  .logo-plate{position:absolute;left:105px;top:70px;width:435px;height:160px;}
  .logo-plate svg{position:absolute;inset:0;}
  .logo-plate .brand-name{
    width:auto;font-size:34px;left:120px;right:30px;top:40px;
  }
  .focus-areas{
    position:absolute;left:50px;top:244px;width:480px;margin:0;padding:0;list-style:none;
    display:grid;grid-template-columns:190px 250px;column-gap:4px;row-gap:1px;
    color:#fff;font-size:13.5px;
  }
  .focus-areas li{display:flex;align-items:center;gap:4px;height:20px;white-space:nowrap;}
  .tick{width:17px;height:18px;flex:none;}
</style>
</head>
<body>

<section class="card card--front" aria-label="Card front">
  <div class="road-photo road-photo--front" role="img" aria-label="Greyscale photo of a winding coastal road and arched bridge over water"></div>
  <p class="tagline">Culture Change with <em>Clarity and Speed</em></p>
  <p class="brand-name">The Summit Ledger</p>
  <div class="contact-panel">
    <svg viewBox="0 0 340 185" width="340" height="185" aria-hidden="true">
      <defs>
        <linearGradient id="panelBlack" x1="0" y1="0" x2="0" y2="1">
          <stop offset="0" stop-color="#3a3a3a"/><stop offset=".5" stop-color="#0c0c0c"/><stop offset="1" stop-color="#2a2a2a"/>
        </linearGradient>
        <linearGradient id="tabSilver" x1="0" y1="0" x2="0" y2="1">
          <stop offset="0" stop-color="#ffffff"/><stop offset="1" stop-color="#bdbdbd"/>
        </linearGradient>
      </defs>
      <path d="M14 41 H300 Q312 41 312 53 V165 Q312 179 298 179 H70 Q58 179 52 168 L2 60 Q-2 41 14 41 Z" fill="url(#panelBlack)"/>
      <path d="M58 0 H240 Q247 0 246 8 L238 64 Q235 78 220 78 H60 Q52 78 52 70 V8 Q52 0 58 0 Z" fill="url(#tabSilver)"/>
    </svg>
    <p class="holder-name">Dan Prewitt</p>
    <ul class="contact-list">
      <li class="phone"><span class="contact-icon"></span>555-417-6290</li>
      <li><span class="contact-icon"></span>Dan@The-Summit-Ledger.example</li>
      <li><span class="contact-icon"></span>www.The-Summit-Ledger.example</li>
    </ul>
  </div>
</section>

<section class="card card--back" aria-label="Card back">
  <div class="road-photo road-photo--back" role="img" aria-label="Greyscale photo of a coastal road leading to an arched bridge"></div>
  <svg class="back-band" viewBox="0 0 575 344" width="575" height="344" aria-hidden="true">
    <defs>
      <linearGradient id="bandRed" x1="0" y1="0" x2="1" y2="1">
        <stop offset="0" stop-color="#1a0205"/><stop offset=".55" stop-color="#8e0a18"/><stop offset="1" stop-color="#2a0306"/>
      </linearGradient>
    </defs>
    <path d="M0 180 Q120 120 300 150 T575 190 V344 H0 Z" fill="url(#bandRed)"/>
    <path d="M0 180 Q120 120 300 150 T575 190" fill="none" stroke="#d0132e" stroke-width="2"/>
  </svg>
  <div class="logo-plate">
    <svg viewBox="0 0 435 160" width="435" height="160" aria-hidden="true">
      <defs>
        <linearGradient id="plateSilver" x1="0" y1="0" x2="1" y2="0">
          <stop offset="0" stop-color="#111"/><stop offset=".25" stop-color="#9a9a9a"/><stop offset=".45" stop-color="#ffffff"/><stop offset="1" stop-color="#cfcfcf"/>
        </linearGradient>
      </defs>
      <path d="M12 8 H420 Q432 8 432 20 V140 Q432 154 418 154 H140 Q115 154 100 130 L78 80 Q64 52 30 48 Q0 46 2 20 Q4 8 12 8 Z" fill="url(#plateSilver)"/>
    </svg>
    <p class="brand-name">The Summit Ledger</p>
  </div>
  <ul class="focus-areas">
    <li><svg class="tick" viewBox="0 0 17 18" aria-hidden="true"><path d="M1 10 L6 16 L16 1 L6 11 Z" fill="#d0132e"/></svg>Performance Improvement</li>
    <li><svg class="tick" viewBox="0 0 17 18" aria-hidden="true"><path d="M1 10 L6 16 L16 1 L6 11 Z" fill="#d0132e"/></svg>Organizational Excellence</li>
    <li><svg class="tick" viewBox="0 0 17 18" aria-hidden="true"><path d="M1 10 L6 16 L16 1 L6 11 Z" fill="#d0132e"/></svg>Strategic Alignment</li>
    <li><svg class="tick" viewBox="0 0 17 18" aria-hidden="true"><path d="M1 10 L6 16 L16 1 L6 11 Z" fill="#d0132e"/></svg>Team Effectiveness</li>
    <li><svg class="tick" viewBox="0 0 17 18" aria-hidden="true"><path d="M1 10 L6 16 L16 1 L6 11 Z" fill="#d0132e"/></svg>Onboarding</li>
    <li><svg class="tick" viewBox="0 0 17 18" aria-hidden="true"><path d="M1 10 L6 16 L16 1 L6 11 Z" fill="#d0132e"/></svg>Leadership Development &amp; Coaching</li>
  </ul>
</section>

<span class="side-label side-label--front">FRONT</span>
<span class="side-label side-label--back">BACK</span>

</body>
</html>
```